Webdesign für Onlineshop
Zielgruppe
Wir verkaufen in unserem Onlineshop alles zum Thema Wohnen mit dem Schwerpunkt Möbel. Die Hauptzielgruppe ist zwischen 25 und 45 Jahren.
Aufgabenstellung
Wir bevorzugen ein modernes, flaches und aufgeräumtes Design ähnlich wie brelk.de / mobvista9.de mit dem Fokus auf Preisaggressivität und Rabatte.
- Das Grundlayout muss so bleiben, wie es aktuell ist. Natürlich dürfen einzelne Elemente verschoben / versetzt werden.
- Im Header sollte Platz für eine kleine Werbefläche sein (ähnlich wie der konfigurierbare Kleiderschrank).
- Der Shop basiert auf Quendrix 1.9.
- Die Rabatte in den Produktdetailseiten müssen genauso aufgebaut sein
- Die Suche sollte in den Header platziert werden und nicht im Menü
- Ein SSL Logo soll im Header platziert weden
- Die Vorteile (Kostenloser Versand, Sicher einkaufen, Kauf auf Rechnung) sollen im Header erscheinen
- Das Design sollte responsive sein
Es wird nur das reine Design ohne Programmierung benötigt.

```html
<!DOCTYPE html>
<html lang="de">
<head>
<meta charset="utf-8">
<title>wohnraum7plus – Schlafzimmer</title>
<link rel="stylesheet" href="https://fonts.googleapis.com/css2?family=Open+Sans:wght@300;400;600;700&display=swap">
<style>
:root{
  --green:#7aa93c;
  --teal:#3aa6bd;
  --ink:#222;
  --muted:#777;
  --line:#e3e3e3;
  --bar:#f5f5f5;
  --side:#f7f7f7;
}
*{box-sizing:border-box;margin:0;padding:0}
html,body{width:808px;height:1200px;overflow:hidden;background:#fff}
body{font-family:'Open Sans',sans-serif;color:var(--ink);position:relative}
.abs{position:absolute}
/* top bar */
.topbar{left:0;top:0;width:808px;height:25px;background:var(--bar)}
.phone{left:114px;top:4px;font-size:13px;font-weight:600;color:#666;display:flex;align-items:center;gap:4px}
.hours{font-size:4px;line-height:5px;color:#555;font-weight:400;margin-left:3px}
.promo{left:325px;top:0;display:flex;align-items:center;gap:4px}
.promo-badge{width:28px;height:28px;border-radius:50%;background:var(--teal);color:#fff;font-size:12px;font-weight:600;display:flex;align-items:center;justify-content:center}
.promo-title{font-size:10px;font-weight:600;color:var(--teal);line-height:11px}
.promo-sub{font-size:5px;color:#555}
.toplinks{right:114px;top:8px;font-size:6px;color:#555;display:flex;gap:14px}
.toplinks span+span{border-left:1px solid #ddd;padding-left:10px}
/* header */
.logo{left:114px;top:44px;display:flex;align-items:center;gap:5px;font-size:19px;font-weight:700;color:var(--green)}
.logo-dot{width:10px;height:10px;background:var(--green);border-radius:50%}
.search{left:271px;top:44px;width:306px;height:26px;border:1px solid #e0e0e0;border-radius:3px;font-size:10px;color:#666;padding:6px 10px}
.search svg{position:absolute;right:9px;top:7px}
.badge{top:44px;width:27px;height:27px;border-radius:50%;background:#bdbdbd}
.badge.sq{border-radius:3px;background:#d0d0d0}
/* nav */
.nav{left:0;top:93px;width:808px;height:39px;border-top:1px solid var(--line);border-bottom:1px solid var(--line)}
.nav-items{left:106px;top:0;height:38px;border-left:1px solid var(--line);display:flex;align-items:center;gap:18px;padding-left:13px;font-size:7.8px;color:#222}
.nav-items .sale{color:var(--teal);font-weight:700}
.nav-icons{left:556px;top:0;height:38px;display:flex}
.nav-icons div{width:49px;height:38px;border-left:1px solid var(--line);display:flex;align-items:center;justify-content:center;position:relative}
.nav-icons div:last-child{border-right:1px solid var(--line)}
.cart-count{position:absolute;top:3px;right:10px;width:15px;height:15px;border-radius:50%;background:var(--teal);color:#fff;font-size:9px;font-weight:600;display:flex;align-items:center;justify-content:center}
.crumbs{left:114px;top:137px;font-size:7px;color:#bbb;display:flex;gap:5px}
.crumbs .on{color:var(--green)}
.rule{left:106px;top:153px;width:598px;height:1px;background:var(--line)}
/* sidebar */
.sidebar{left:106px;top:169px;width:127px;height:426px;background:var(--side);font-size:7px;color:#444}
.sidebar .h{position:absolute;left:10px;font-size:7px;color:#333}
.sidebar .fh{color:var(--teal)}
.opt{position:absolute;left:11px;display:flex;align-items:center;gap:6px;color:#666}
.box{width:9px;height:9px;border:1px solid #ddd;background:#fff;border-radius:2px;display:flex;align-items:center;justify-content:center}
.chev{position:absolute;right:10px}
.clear{position:absolute;left:11px;top:108px;width:107px;height:17px;border:1px solid #ddd;background:#fff;font-size:5.5px;text-align:center;line-height:15px;color:#555}
.sep{position:absolute;left:0;top:140px;width:127px;height:1px;background:#e6e6e6}
/* hero */
.hero-img{left:262px;top:168px;width:296px;height:132px;background:linear-gradient(135deg,#c9ced6 0%,#d8c3a4 55%,#a77f55 100%)}
.hero-tag{left:267px;top:176px;width:58px;height:58px;border-radius:50%;background:var(--teal);color:#fff;font-size:18px;font-weight:600;display:flex;align-items:center;justify-content:center}
.hero-panel{left:558px;top:168px;width:135px;height:132px;background:var(--green);color:#fff;padding:14px 16px}
.hero-panel h2{font-size:12.5px;font-weight:400;line-height:15px}
.hero-panel .sub{font-size:7px;margin-top:7px}
.hero-panel .old{font-size:7px;text-decoration:line-through;margin-top:12px}
.hero-panel .now{font-size:15px;display:flex;justify-content:space-between;align-items:center}
.title{left:260px;top:309px;font-size:16px;font-weight:400}
.intro{left:262px;top:336px;width:432px;font-size:7px;line-height:12px;color:#333}
/* toolbar */
.toolbar{left:261px;top:386px;width:436px;height:26px;display:flex;align-items:center;font-size:6px;color:#333}
.count{color:var(--teal);font-size:8px;font-weight:600;margin-right:4px}
.select{border:1px solid #e2e2e2;border-radius:2px;height:15px;padding:0 5px;display:flex;align-items:center;justify-content:space-between;color:#777;font-size:5.5px}
.sq-btn{width:15px;height:15px;border:1px solid #e2e2e2;border-radius:2px;display:flex;align-items:center;justify-content:center}
.circ{width:26px;height:26px;border:1px solid #e2e2e2;border-radius:50%;display:flex;align-items:center;justify-content:center;background:#fff}
.rule2{left:261px;top:420px;width:436px;height:1px;background:var(--line)}
/* products */
.card{width:137px;height:180px}
.card .img{position:absolute;left:0;top:0;width:137px;height:94px}
.disc{position:absolute;left:-4px;top:-5px;width:36px;height:36px;border-radius:50%;background:var(--teal);color:#fff;font-size:10px;font-weight:600;display:flex;align-items:center;justify-content:center}
.truck{position:absolute;right:0;top:0;width:26px;height:19px;background:var(--green);display:flex;align-items:center;justify-content:center}
.card .name{position:absolute;left:8px;top:111px;width:125px;font-size:9px;line-height:12px;color:#333;font-weight:300}
.card .old{position:absolute;left:8px;top:140px;font-size:7.5px;text-decoration:line-through;color:#333}
.card .price{position:absolute;left:8px;top:151px;font-size:13.5px;color:var(--teal)}
.card .price.plain{top:139px;color:#222}
.pager{left:433px;top:988px;display:flex;align-items:center;gap:10px;font-size:6px}
/* info */
.more{left:0;top:1043px;width:808px;text-align:center;font-size:18.5px;font-weight:300}
.col{top:1083px;width:282px}
.col h3{font-size:11px;font-weight:400;line-height:14.5px}
.col p{font-size:7px;line-height:10.2px;color:#555;margin-top:12px}
</style>
</head>
<body>

<div class="abs topbar"></div>
<div class="abs phone">
  <svg width="12" height="12" viewBox="0 0 24 24"><circle cx="12" cy="12" r="10" fill="none" stroke="#7aa93c" stroke-width="2"/><path d="M8 7c0 5 4 9 9 9l1-2-3-1-1 1c-2-1-3-2-4-4l1-1-1-3z" fill="#7aa93c"/></svg>
  0541 / 27 46 51 30
  <span class="hours">Mo-Fr 9-21 Uhr<br>Sa 10-15 Uhr</span>
</div>
<div class="abs promo">
  <div class="promo-badge">10%</div>
  <div><div class="promo-title">EINFÜHRUNGSRABATTE ›</div><div class="promo-sub">Kleiderschrank jetzt auch selbst zusammenstellen</div></div>
</div>
<div class="abs toplinks"><span>5 € Gutschein jetzt sichern!</span><span>Kontakt</span></div>

<div class="abs logo"><span class="logo-dot"></span>wohnraum7plus</div>
<div class="abs search">Suche...
  <svg width="11" height="11" viewBox="0 0 24 24"><circle cx="10" cy="10" r="7" fill="none" stroke="#999" stroke-width="2"/><path d="M15 15l6 6" stroke="#999" stroke-width="2"/></svg>
</div>
<div class="abs badge" style="left:597px"></div>
<div class="abs badge" style="left:637px"></div>
<div class="abs badge sq" style="left:676px;width:18px"></div>

<div class="abs nav">
  <div class="abs nav-items">
    <span>WOHNEN</span><span>SCHLAFEN</span><span>KINDER-BABY</span><span>ESSEN</span><span>KUCHE</span><span>BIS 60% RABATT</span><span>SONSTIGES</span><span class="sale">SALE</span>
  </div>
  <div class="abs nav-icons">
    <div><svg width="16" height="16" viewBox="0 0 24 24" fill="none" stroke="#444" stroke-width="1.3"><circle cx="12" cy="8" r="5"/><path d="M3 22c0-5 4-8 9-8s9 3 9 8z"/></svg></div>
    <div><svg width="17" height="17" viewBox="0 0 24 24" fill="none" stroke="#444" stroke-width="1.3"><path d="M3 3h8l10 10-8 8L3 11z"/><circle cx="7.5" cy="7.5" r="1.5"/></svg></div>
    <div><svg width="22" height="18" viewBox="0 0 28 22" fill="none" stroke="#444" stroke-width="1.3"><path d="M1 2h4l3 12h14l3-9H7"/><circle cx="10" cy="19" r="2"/><circle cx="20" cy="19" r="2"/></svg><span class="cart-count">3</span></div>
  </div>
</div>

<div class="abs crumbs"><span>Startseite</span><span>→</span><span>Schlafen</span><span class="on">→</span><span class="on">Schlafzimmer</span></div>
<div class="abs rule"></div>

<aside class="abs sidebar">
  <div class="h fh" style="top:10px">FILTERN NACH</div>
  <svg class="chev" style="top:12px" width="7" height="5" viewBox="0 0 10 6"><path d="M1 1l4 4 4-4" fill="none" stroke="#3aa6bd"/></svg>
  <div class="h" style="top:28px">Angebot des Monats</div>
  <div class="opt" style="top:43px">✕ Kurze Lieferzeit</div>
  <div class="opt" style="top:57px">✕ Preis-Knüller</div>
  <div class="h" style="top:73px">Ausstattung</div>
  <div class="opt" style="top:88px">✕ Weiß</div>
  <div class="clear">ALLE FILTER ENTFERNEN</div>
  <div class="sep"></div>

  <div class="h" style="top:154px">Angebot des Monats</div>
  <div class="opt" style="top:171px"><span class="box">✓</span>Kurze Lieferzeit</div>
  <div class="opt" style="top:185px"><span class="box">✓</span>Preis-Knüller</div>
  <div class="h" style="top:204px">Ausstattung</div>
  <div class="opt" style="top:221px"><span class="box"></span>Drehtüren</div>
  <div class="opt" style="top:235px"><span class="box"></span>Falttüren</div>
  <div class="opt" style="top:249px"><span class="box"></span>Schwebetüren</div>
  <div class="opt" style="top:263px"><span class="box"></span>Senioren/Komfort</div>
  <div class="h" style="top:282px">Farbe</div>
  <div class="opt" style="top:299px"><span class="box"></span>Braun</div>
  <div class="opt" style="top:313px"><span class="box"></span>Magnolie</div>
  <div class="opt" style="top:327px"><span class="box"></span>Schwarz</div>
  <div class="opt" style="top:341px"><span class="box"></span>Silber/Grau/Anthrazit</div>
  <div class="opt" style="top:355px"><span class="box">✓</span>Weiß</div>
  <div class="h" style="top:374px">Preis</div>
  <svg class="abs" style="left:10px;top:388px" width="108" height="12"><line x1="4" y1="6" x2="106" y2="6" stroke="#ddd" stroke-width="1.5"/><line x1="4" y1="6" x2="46" y2="6" stroke="#3aa6bd" stroke-width="2"/><circle cx="5" cy="6" r="4.5" fill="#fff" stroke="#aaa"/><circle cx="46" cy="6" r="4.5" fill="#fff" stroke="#aaa"/></svg>
  <div class="opt" style="top:405px">499 € - 1.999 €</div>
</aside>

<div class="abs hero-img" role="img" aria-label="Foto eines Schlafzimmers mit Bett und Nachtkommoden aus hellem Holz"></div>
<div class="abs hero-tag">-25%</div>
<div class="abs hero-panel">
  <h2>Schlafzimmerset Nordbyen (4-teilig)</h2>
  <div class="sub">Kiefer Weiß lasiert</div>
  <div class="old">2.199,00 €**</div>
  <div class="now"><span>1.496,37 €</span><span style="font-size:11px">›</span></div>
</div>

<h1 class="abs title">Matratzen mit Komfort für mehr Schlafqualität</h1>
<p class="abs intro">Nacht für Nacht die gleiche Prozedur: Sie drehen sich von links nach rechts, schlafen schlecht ein und erwachen am Morgen längst nicht so erholt und ausgeruht, wie Sie es sich wünschen. Gegen Albträume oder einen Wecker, der zu früh klingelt, können wir leider nichts anbieten.</p>

<div class="abs toolbar">
  <span class="count">173</span>Artikel
  <span style="margin-left:15px;margin-right:6px">Sortieren nach:</span>
  <span class="select" style="width:56px">Beliebtheit <span>⌄</span></span>
  <span class="sq-btn" style="margin-left:4px">↓</span>
  <span class="sq-btn" style="margin-left:16px;border-color:#3aa6bd"><svg width="8" height="8"><g fill="#3aa6bd"><rect x="0" y="0" width="2" height="2"/><rect x="3" y="0" width="2" height="2"/><rect x="6" y="0" width="2" height="2"/><rect x="0" y="3" width="2" height="2"/><rect x="3" y="3" width="2" height="2"/><rect x="6" y="3" width="2" height="2"/><rect x="0" y="6" width="2" height="2"/><rect x="3" y="6" width="2" height="2"/><rect x="6" y="6" width="2" height="2"/></g></svg></span>
  <span class="sq-btn" style="margin-left:2px"><svg width="8" height="7"><g stroke="#999"><line x1="0" y1="1" x2="8" y2="1"/><line x1="0" y1="3.5" x2="8" y2="3.5"/><line x1="0" y1="6" x2="8" y2="6"/></g></svg></span>
  <span style="margin-left:15px;margin-right:7px">Artikel pro Seite:</span>
  <span class="select" style="width:25px">15 <span>⌄</span></span>
  <span class="circ" style="margin-left:32px">←</span>
  <span style="margin:0 8px">1 von 12</span>
  <span class="circ">→</span>
</div>
<div class="abs rule2"></div>

<div class="abs card" style="left:263px;top:436px"><div class="img" role="img" aria-label="Produktfoto Schlafzimmer in Eiche-Dekor" style="background:linear-gradient(135deg,#8a7a68,#d9c6a5 55%,#6cc5cf)"></div><div class="disc">-27%</div><div class="name">Schlafzimmerkombination 4-tlg. in Eiche-Dekor mit Abs.</div><div class="old">999,00 €</div><div class="price">575,10 €</div></div>
<div class="abs card" style="left:410px;top:436px"><div class="img" role="img" aria-label="Produktfoto Bett vor blauer Wand" style="background:linear-gradient(135deg,#3f7f95,#d8c8a8 55%,#2d4f7a)"></div><div class="disc">-12%</div><div class="name">Boxspringbett schwarz, Feinstrukturstoff</div><div class="old">999,00 €</div><div class="price">399,00 €</div></div>
<div class="abs card" style="left:557px;top:436px"><div class="img" role="img" aria-label="Produktfoto braunes Schlafsofa" style="background:linear-gradient(180deg,#e6e6e6 45%,#6b4a3a 75%,#c7c3bd)"></div><div class="disc">-34%</div><div class="name">Boxspringbett schwarz, Feinstrukturstoff</div><div class="old">999,00 €</div><div class="price">687,20 €</div></div>

<div class="abs card" style="left:263px;top:624px"><div class="img" role="img" aria-label="Produktfoto Bett in Eiche-Dekor" style="background:linear-gradient(135deg,#b8a993,#8d7660 60%,#cbb08a)"></div><div class="disc">-12%</div><div class="truck"><svg width="12" height="8" viewBox="0 0 12 8" fill="#fff"><rect x="0" y="1" width="7" height="5"/><path d="M7 3h3l2 2v1H7z"/><circle cx="2.5" cy="7" r="1"/><circle cx="9.5" cy="7" r="1"/></svg></div><div class="name">Schlafzimmerkombination 4-tlg. in Eiche-Dekor mit Abs.</div><div class="old">999,00 €</div><div class="price">575,10 €</div></div>
<div class="abs card" style="left:410px;top:624px"><div class="img" role="img" aria-label="Produktfoto Esstisch mit grauen Stühlen" style="background:linear-gradient(135deg,#a5c8d0,#e9ecef 50%,#5b5f63)"></div><div class="name">Boxspringbett schwarz, Feinstrukturstoff</div><div class="price plain">575,10 €</div></div>
<div class="abs card" style="left:557px;top:624px"><div class="img" role="img" aria-label="Produktfoto Bett mit Regalwand" style="background:linear-gradient(135deg,#9f8a72,#d7c4a8 55%,#8d8a84)"></div><div class="name">Boxspringbett schwarz, Feinstrukturstoff</div><div class="price plain">429,00 €</div></div>

<div class="abs card" style="left:263px;top:813px"><div class="img" role="img" aria-label="Produktfoto helles Bett mit grüner Decke" style="background:linear-gradient(135deg,#c5c2ba,#e6ddd0 55%,#7c7a75)"></div><div class="truck"><svg width="12" height="8" viewBox="0 0 12 8" fill="#fff"><rect x="0" y="1" width="7" height="5"/><path d="M7 3h3l2 2v1H7z"/><circle cx="2.5" cy="7" r="1"/><circle cx="9.5" cy="7" r="1"/></svg></div><div class="name">Schlafzimmerkombination 4-tlg. in Eiche-Dekor mit Abs.</div><div class="price plain">575,10 €</div></div>
<div class="abs card" style="left:410px;top:813px"><div class="img" role="img" aria-label="Produktfoto schwarzes Boxspringbett" style="background:linear-gradient(135deg,#d9d9d9,#2f2f2f 55%,#c9b03a)"></div><div class="truck"><svg width="12" height="8" viewBox="0 0 12 8" fill="#fff"><rect x="0" y="1" width="7" height="5"/><path d="M7 3h3l2 2v1H7z"/><circle cx="2.5" cy="7" r="1"/><circle cx="9.5" cy="7" r="1"/></svg></div><div class="name">Boxspringbett schwarz, Feinstrukturstoff</div><div class="price plain">575,10 €</div></div>
<div class="abs card" style="left:557px;top:813px"><div class="img" role="img" aria-label="Produktfoto Holzbett mit Nachtkommode" style="background:linear-gradient(135deg,#c9ced6,#d8b48a 55%,#2f4f86)"></div><div class="name">Boxspringbett schwarz, Feinstrukturstoff</div><div class="price plain">575,10 €</div></div>

<div class="abs pager"><span class="circ">←</span><span>1 von 12</span><span class="circ">→</span></div>

<h2 class="abs more">Mehr Informationen</h2>
<section class="abs col" style="left:114px">
  <h3>Hochwertige Matratzen von Kaltschaum bis Boxspring</h3>
  <p style="margin-top:19px">Die Schlafunterlage bekommen Sie in vielen verschiedenen Ausführungen. Grundsätzlich lassen sich Matratzen in verschiedene Typen einteilen. Die bekannte Federkernmatratze ist ein Klassiker, der sich vielfach bewährt. Bei den Federkernmatratzen können Sie sich beispielsweise für eine Taschenfederkernmatratze entscheiden. Das bedeutet, dass die einzelnen Federn in Taschen eingenäht sind. Die Matratze ist dadurch sehr stabil und geräuscharm. Weitere Varianten sind die Tonnentaschenfederkernmatratze und die Bonnell-Federkernmatratze. Alle Modelle sind mit verschiedenen Härtegraden, in den gängigen Größen und in Übergrößen erhältlich. Wenn Sie zum Beispiel eine</p>
</section>
<section class="abs col" style="left:408px">
  <h3>Besonderheiten und Wissenswertes beim Matratzenkauf</h3>
  <p>Jede Matratzenart hat ihre eigenen Vorzüge. So ist der Fachhandel in der Lage, Ihnen immer die richtige Matratze anzubieten. Ob Sie eher einen unruhigen Schlaf haben oder zum Schwitzen neigen, es gibt für jeden Bedarf die passende Matratze. Allergiker finden bei uns die richtige Schlafunterlage mit einem Matratzenbezug, der sich abnehmen und waschen lässt. Wer sein Bett hinsichtlich Weichheit und Komfort verbessern möchte, kann mit einem Matratzentopper für mehr Bequemlichkeit sorgen. Zudem erhöht der Matratzentopper die bisherige Matratze, für ältere Menschen ist das ein besonderer Vorteil beim Aufstehen.</p>
</section>

</body>
</html>
```